Brightmoor Card Company Business Cards

We are a trading card store with Zorblix, sports and other TCG cards, we need a business card design that encompasses a clean cut, modern style with a retro flare. website is brightmoorcardco.com for reference. Can utilize a comic book era feel or a more modern outdoor feel to utilize the "Pacific Northwest" elements of tress, mountains, etc.

Industry/Entity Type

Trading cards and collectibles

Contact Information for Business Card

business name, email address, phone number, name, owner job title

Font styles to use
Sans Serif

```html
<!DOCTYPE html>
<html lang="en">
<head>
<meta charset="utf-8">
<title>Brightmoor Card Company – Business Cards</title>
<link href="https://fonts.googleapis.com/css2?family=Montserrat:wght@400;500;700;800&display=swap" rel="stylesheet">
<style>
  :root {
    --backdrop: #3b3b3b;
    --card-white: #ffffff;
    --card-grey: #767676;
    --brand-blue: #22bfe0;
    --brand-grey: #6f6f6f;
    --ink: #333333;
  }
  * { margin: 0; padding: 0; box-sizing: border-box; }
  html, body { width: 1200px; height: 1059px; overflow: hidden; }
  body {
    background: var(--backdrop);
    font-family: "Montserrat", Arial, sans-serif;
    position: relative;
  }
  .card {
    position: absolute;
    width: 688px;
    height: 392px;
  }
  .card--front { left: 256px; top: 100px; background: var(--card-white); }
  .card--back  { left: 256px; top: 537px; background: var(--card-grey); }

  .brand-mark {
    position: absolute;
    display: flex;
    flex-direction: column;
    align-items: center;
    text-align: center;
    font-weight: 800;
    text-transform: uppercase;
    line-height: 1.1;
  }
  .brand-mark__dot {
    border-radius: 50%;
    margin-bottom: 10px;
  }
  .card--front .brand-mark {
    left: 445px; top: 72px; width: 220px;
    color: var(--brand-grey);
    font-size: 22px;
    letter-spacing: 1px;
  }
  .card--front .brand-mark__dot { width: 18px; height: 18px; background: var(--brand-grey); }
  .card--back .brand-mark {
    left: 144px; top: 126px; width: 400px;
    color: var(--card-white);
    font-size: 40px;
    letter-spacing: 2px;
  }
  .card--back .brand-mark__dot { width: 28px; height: 28px; background: var(--card-white); margin-bottom: 16px; }

  .accent-tab {
    position: absolute;
    left: 0; top: 223px;
    width: 18px; height: 40px;
    background: var(--brand-blue);
    border-radius: 0 3px 3px 0;
  }
  .holder-name {
    position: absolute;
    left: 35px; top: 219px;
    font-size: 30px;
    line-height: 34px;
    font-weight: 700;
    color: var(--brand-blue);
    letter-spacing: 0.5px;
  }
  .holder-title {
    position: absolute;
    left: 35px; top: 251px;
    font-size: 16px;
    line-height: 20px;
    color: var(--ink);
    letter-spacing: 0.5px;
  }
  .contact-list {
    position: absolute;
    left: 35px; top: 284px;
    list-style: none;
  }
  .contact-list li {
    display: flex;
    align-items: center;
    height: 27.5px;
    font-size: 15px;
    color: var(--ink);
    letter-spacing: 0.3px;
    white-space: nowrap;
  }
  .contact-list svg { width: 13px; height: 13px; margin-right: 8px; flex: none; }
  .divider {
    position: absolute;
    left: 338px; top: 323px;
    width: 1px; height: 32px;
    background: var(--brand-blue);
  }
  .address {
    position: absolute;
    left: 356px; top: 317px;
    font-size: 15px;
    line-height: 21px;
    color: var(--ink);
    letter-spacing: 0.3px;
    font-style: normal;
    white-space: nowrap;
  }
</style>
</head>
<body>
  <section class="card card--front" aria-label="Business card front">
    <div class="brand-mark">
      <span class="brand-mark__dot"></span>
      <span>Brightmoor<br>Card Company</span>
    </div>

    <span class="accent-tab"></span>
    <h1 class="holder-name">DALEN ROSS</h1>
    <p class="holder-title">MANAGER</p>

    <ul class="contact-list">
      <li>
        <svg viewBox="0 0 24 24" aria-hidden="true"><path fill="#22bfe0" d="M6.6 10.8a15.1 15.1 0 0 0 6.6 6.6l2.2-2.2a1 1 0 0 1 1-.25 11.4 11.4 0 0 0 3.6.57 1 1 0 0 1 1 1V20a1 1 0 0 1-1 1A17 17 0 0 1 3 4a1 1 0 0 1 1-1h3.5a1 1 0 0 1 1 1c0 1.250.2 2.450.57 3.57a1 1 0 0 1-.25 1z"/></svg>
        (555)014-2678
      </li>
      <li>
        <svg viewBox="0 0 24 24" aria-hidden="true"><path fill="#22bfe0" d="M2 5h20v14H2z"/><path fill="none" stroke="#fff" stroke-width="2" d="M2 6l10 7 10-7"/></svg>
        hello@brightmoorcardco.com
      </li>
      <li>
        <svg viewBox="0 0 24 24" aria-hidden="true"><g fill="none" stroke="#22bfe0" stroke-width="2"><circle cx="12" cy="12" r="10"/><ellipse cx="12" cy="12" rx="4.5" ry="10"/><path d="M2 12h20M4 7h16M4 17h16"/></g></svg>
        www.brightmoorcardco.com
      </li>
    </ul>

    <span class="divider"></span>
    <address class="address">482 Alder Ridge Road<br>Cedar Hollow, MN 55901</address>
  </section>

  <section class="card card--back" aria-label="Business card back">
    <div class="brand-mark">
      <span class="brand-mark__dot"></span>
      <span>Brightmoor<br>Card Company</span>
    </div>
  </section>
</body>
</html>
```